Meadowlark Learning Growth Partners (MLGP)

This is a professional business card. Logo and picture are a must on the front of the card. I am an educational consultant. I have been consulting for the past three years for a company. I am now opening my own company. My goal for my consulting company is to eventually consult all over America.

Target Market(s)

Educators, schools, professionals

Industry/Entity Type

Consulting

Contact Information for Business Card

Picture/logo on front, simple modern design

Font styles to use
Serif

Colors
85abd2
0355a3
3176b5
cedeed

Requirements
Must have
• picture, logo,
• Odessa Pruitt, Ed.S
• address 5073 Cormorant ridge Dr. Nashville, TN 37940
• Cell:616-555-0148
• Office: 629-555-0172
• www.Mlgpedu.example
• pruittodessa@mailbox.example

```html
<!DOCTYPE html>
<html lang="en">
<head>
<meta charset="utf-8">
<title>MLGP Business Card</title>
<link rel="stylesheet" href="https://fonts.googleapis.com/css2?family=Lexend:wght@400;500;600;700&family=Roboto:wght@400;500&display=swap">
<style>
  :root {
    --navy: #0a3d86;
    --navy-deep: #083170;
    --brand: #0355a3;
    --mid: #3176b5;
    --sky: #85abd2;
    --mist: #cedeed;
    --paper: #ffffff;
    --paper-shade: #eef0f3;
    --stage: #e4e7ec;
  }
  * { box-sizing: border-box; margin: 0; padding: 0; }
  html, body { width: 1200px; height: 900px; overflow: hidden; }
  body { background: var(--stage); position: relative; font-family: "Lexend", sans-serif; }

  .card {
    position: absolute;
    left: 280px;
    width: 640px;
    height: 366px;
    border-radius: 18px;
    overflow: hidden;
    box-shadow: 0 10px 30px rgba(0, 0, 0, 0.18);
  }
  .card--front { top: 50px; background: linear-gradient(180deg, var(--paper) 0%, var(--paper-shade) 100%); }
  .card--back { top: 480px; background: linear-gradient(135deg, var(--navy) 0%, var(--navy-deep) 100%); }

  .front-shapes { position: absolute; inset: 0; }

  .brand { position: absolute; display: flex; align-items: center; }
  .brand__mark { width: 18px; height: 18px; border-radius: 50%; background: var(--brand); margin-right: 10px; }
  .brand__name { font-weight: 700; font-size: 30px; letter-spacing: 3px; color: var(--brand); }
  .brand__rule { width: 1.5px; height: 58px; background: var(--brand); margin: 0 12px 0 16px; }
  .brand__tagline { font-weight: 600; font-size: 11.5px; line-height: 1.2; color: var(--brand); }

  .card--front .brand { left: 36px; top: 22px; }

  .person { position: absolute; left: 36px; top: 112px; color: var(--paper); }
  .person__name { font-size: 24px; font-weight: 500; letter-spacing: 0.2px; }
  .person__title { font-size: 13px; font-weight: 400; opacity: 0.85; margin-top: 2px; }

  .contacts { position: absolute; left: 36px; top: 200px; list-style: none; font-family: "Roboto", sans-serif; color: var(--brand); font-size: 15px; }
  .contacts li { display: flex; align-items: center; height: 26px; }
  .contacts svg { width: 12px; height: 12px; margin-right: 10px; flex: none; }

  .card--back .brand { left: 150px; top: 110px; }
  .card--back .brand__mark { background: var(--mist); width: 22px; height: 22px; }
  .card--back .brand__name { color: var(--mist); font-size: 40px; }
  .card--back .brand__rule { background: var(--mist); height: 84px; }
  .card--back .brand__tagline { color: var(--mist); font-size: 15px; }

  .address { position: absolute; left: 150px; top: 240px; display: flex; align-items: center; color: var(--mist); font-family: "Roboto", sans-serif; font-size: 15px; }
  .address svg { width: 12px; height: 14px; margin-right: 8px; }
</style>
</head>
<body>

<section class="card card--front">
  <svg class="front-shapes" width="640" height="366" viewBox="0 0 640 366">
    <defs>
      <linearGradient id="portraitTone" x1="0" y1="0" x2="1" y2="1">
        <stop offset="0" stop-color="#3f73c4"/>
        <stop offset="1" stop-color="#2a5aa8"/>
      </linearGradient>
    </defs>
    <rect class="name-band" x="0" y="100" width="640" height="66" fill="#0a3d86"/>
    <circle class="portrait-ring" cx="468" cy="208" r="152" fill="#0a3d86"/>
    <circle cx="468" cy="208" r="144" fill="url(#portraitTone)" role="img" aria-label="Portrait photo of Odessa Pruitt"/>
  </svg>

  <div class="brand">
    <span class="brand__mark"></span>
    <span class="brand__name">MLGP</span>
    <span class="brand__rule"></span>
    <span class="brand__tagline">Meadowlark<br>Learning<br>Growth<br>Partners</span>
  </div>

  <div class="person">
    <div class="person__name">Odessa Pruitt, Ed.S</div>
    <div class="person__title">Director</div>
  </div>

  <ul class="contacts">
    <li><svg viewBox="0 0 12 12"><rect x="3" y="0.5" width="6" height="11" rx="1.2" fill="none" stroke="currentColor" stroke-width="1.2"/><circle cx="6" cy="9.5" r="0.7" fill="currentColor"/></svg>616-555-0148</li>
    <li><svg viewBox="0 0 12 12"><path d="M2.5 1 L4.5 1 L5.3 3.6 L4 4.6 Q5 7 7.4 8 L8.4 6.7 L11 7.5 L11 9.5 Q11 11 9.5 11 Q1 10 1 2.5 Q1 1 2.5 1 Z" fill="currentColor"/></svg>629-555-0172</li>
    <li><svg viewBox="0 0 12 12"><rect x="0.8" y="2" width="10.4" height="8" rx="1" fill="none" stroke="currentColor" stroke-width="1.2"/><path d="M1 2.5 L6 6.5 L11 2.5" fill="none" stroke="currentColor" stroke-width="1.2"/></svg>www.Mlgpedu.example</li>
    <li><svg viewBox="0 0 12 12"><circle cx="6" cy="6" r="5" fill="none" stroke="currentColor" stroke-width="1.1"/><ellipse cx="6" cy="6" rx="2.2" ry="5" fill="none" stroke="currentColor" stroke-width="1"/><path d="M1 6 H11" stroke="currentColor" stroke-width="1"/></svg>pruittodessa@mailbox.example</li>
  </ul>
</section>

<section class="card card--back">
  <div class="brand">
    <span class="brand__mark"></span>
    <span class="brand__name">MLGP</span>
    <span class="brand__rule"></span>
    <span class="brand__tagline">Meadowlark<br>Learning<br>Growth<br>Partners</span>
  </div>
  <div class="address">
    <svg viewBox="0 0 12 14"><path d="M6 0.5 A5 5 0 0 1 11 5.5 C11 9 6 13.5 6 13.5 C6 13.5 1 9 1 5.5 A5 5 0 0 1 6 0.5 Z" fill="currentColor"/><circle cx="6" cy="5.5" r="1.8" fill="#0a3d86"/></svg>
    5073 Cormorant ridge Dr. Nashville, TN 37940
  </div>
</section>

</body>
</html>
```